Online Cooking App Pitch Deck- (THIS IS NOT A FOOD BUSINESS OR FOOD SERVICE, NO FOOD PICTURES)

Project Goal:
Design a visually compelling pitch deck to be used for securing investment. Looking for the pitch deck to be about the design using shapes, colors, fonts and sizes. Must be creative yet simple and clean.
Color Palette:
https://huebrik.io/ff3800-ffe2db-fefefa-2d3e50-010b13

(We want most screens to use #FEFEFA)

This is the current pitch deck we need simplified and redesigned (USE TEXT IN THE VANDREL LINK TO SHOW IN YOUR DESIGN):

https://files.vandrel.net/slides/d/7QpLmZ2kTr84NwXaVbcY0-hoxjdEuvwKt/view?mode=share&uid=503921846170259384712&fmt=true&sd=true

Project is now guaranteed. Remember use the text in the vandrel link in powerpoint design. Use a little more color not just the logo color. Do not use any pictures of food this is not food related business. We care more about style and design of shapes, text, color fonts.

Target Market(s)

Investors (venture capitalists, angel investors) interested in innovative technology solutions within the food industry.

Font styles to use
Serif
Sans Serif

Requirements
Nice to have
• Simple, abstract background non distracting but complementary.
Should not have
• No pictures

```html
<!DOCTYPE html>
<html lang="en">
<head>
<meta charset="utf-8">
<title>Simmerly – Online Cooking App Deck</title>
<link rel="stylesheet" href="https://fonts.googleapis.com/css2?family=Poppins:wght@400;500;600;700;800&family=Merriweather:wght@400;700;900&display=swap">
<style>
:root{
  --orange:#ff3800;
  --blush:#ffe2db;
  --paper:#fefefa;
  --navy:#2d3e50;
  --ink:#010b13;
  --board:#d9d9d9;
  --muted:#7d858c;
}
*{margin:0;padding:0;box-sizing:border-box}
html,body{width:1200px;height:1162px;overflow:hidden;background:var(--board)}
body{position:relative;font-family:"Poppins",sans-serif;color:var(--ink)}
.slide{position:absolute;width:359px;height:202px;background:var(--paper);overflow:hidden}
.slide>*{position:absolute}
.col1{left:48px}.col2{left:420px}.col3{left:793px}
.row1{top:50px}.row2{top:264px}.row3{top:483px}.row4{top:701px}.row5{top:921px}
.dark{background:var(--navy);color:#fff}
.serif{font-family:"Merriweather",serif}
.accent{color:var(--orange)}
.brand-bar{left:0;top:13px;width:4px;height:12px;background:var(--orange)}
.brand{left:9px;top:13px;font-size:8px;font-weight:500;line-height:12px}
.site{left:9px;bottom:9px;font-size:4.5px;letter-spacing:1.4px}
.page{right:10px;bottom:8px;font-size:5px}
.tiny{font-size:3.6px;line-height:4.6px;color:var(--muted)}
.h-sans{font-weight:700;line-height:1.05}
.chip{background:var(--orange);color:#fff}
.card{background:#fff;box-shadow:0 1px 3px rgba(1,11,19,.18)}
/* abstract shape panels */
.motif-warm{background:
  radial-gradient(circle at 78% 28%,var(--orange) 0 16%,transparent 16.5%),
  radial-gradient(circle at 18% 86%,var(--navy) 0 24%,transparent 24.5%),
  var(--blush)}
.motif-cool{background:
  radial-gradient(circle at 22% 24%,var(--blush) 0 14%,transparent 14.5%),
  radial-gradient(circle at 85% 90%,var(--orange) 0 28%,transparent 28.5%),
  var(--navy)}
.motif-soft{background:
  radial-gradient(circle at 50% 50%,transparent 0 24%,var(--orange) 24.5% 27%,transparent 27.5%),
  radial-gradient(circle at 88% 12%,var(--navy) 0 14%,transparent 14.5%),
  var(--blush)}
.motif-stripe{background:
  repeating-linear-gradient(135deg,transparent 0 14px,rgba(255,56,0,.18) 14px 16px),
  var(--blush)}
.icon-box{width:21px;height:21px;display:flex;align-items:center;justify-content:center}
.food-card{width:64px;height:37px;border-radius:4px}
.food-icon{width:11px;height:11px;border:1.5px solid var(--orange)}
.food-title{font-size:6px;font-weight:600}
.food-text{font-size:3.3px;line-height:4px;width:38px;color:var(--muted)}
</style>
</head>
<body>

<!-- Row 1 -->
<section class="slide dark row1 col1">
  <div class="motif-warm" aria-hidden="true" style="left:230px;top:0;width:129px;height:202px;border-radius:60px 0 0 60px"></div>
  <div style="left:27px;top:24px;font-size:17px;font-weight:500">Simmerly</div>
  <div class="serif" style="left:28px;top:76px;font-size:8px;font-weight:700">Presentation</div>
  <div class="serif accent" style="left:28px;top:84px;font-size:31px;font-weight:900">Business</div>
  <div class="serif" style="left:28px;top:118px;font-size:22px;font-weight:700">Marketing</div>
  <svg style="left:22px;top:178px" width="20" height="6"><circle cx="3" cy="3" r="2" fill="#fff"/><circle cx="10" cy="3" r="2" fill="#ff3800"/><circle cx="17" cy="3" r="2" fill="#fff"/></svg>
</section>

<section class="slide row1 col2" style="background:var(--ink);color:#fff">
  <svg style="left:0;top:0" width="359" height="110" aria-hidden="true">
    <circle cx="20" cy="22" r="16" fill="#2d3e50"/>
    <circle cx="64" cy="28" r="14" fill="#ffe2db" opacity=".25"/>
    <circle cx="110" cy="26" r="17" fill="#ff3800"/>
    <circle cx="185" cy="45" r="30" fill="#2d3e50"/>
    <circle cx="185" cy="45" r="18" fill="none" stroke="#ff3800" stroke-width="3"/>
    <circle cx="250" cy="40" r="26" fill="#ff3800" opacity=".85"/>
    <circle cx="320" cy="24" r="17" fill="#ffe2db"/>
    <circle cx="346" cy="60" r="8" fill="#ff3800"/>
  </svg>
  <div style="left:0;width:359px;top:120px;text-align:center;font-size:26px;font-weight:500">Simmerly</div>
  <div class="chip" style="left:128px;top:159px;width:106px;height:14px;border-radius:7px;font-size:8px;font-weight:700;text-align:center;line-height:14px">Online Cooking App</div>
</section>

<section class="slide row1 col3">
  <div class="brand-bar"></div><div class="brand">Simmerly</div>
  <div class="h-sans" style="left:31px;top:48px;font-size:16px;font-weight:600;line-height:19px">What <span class="accent">We<br>Have</span><br>Achieved</div>
  <p class="tiny" style="left:31px;top:118px;width:110px">Cooking classes streamed live from real kitchens to any home. Learners follow chefs step by step and cook along.<br><br>Every lesson is short, guided and easy to repeat later on demand.</p>
  <div class="motif-soft" aria-hidden="true" style="left:164px;top:44px;width:195px;height:130px"></div>
  <div style="left:164px;top:174px;width:74px;height:4px;background:var(--orange)"></div>
  <div class="site">www.website.com</div><div class="page">2</div>
</section>

<!-- Row 2 -->
<section class="slide row2 col1">
  <div class="brand-bar"></div><div class="brand">Simmerly</div>
  <div class="h-sans" style="left:26px;top:46px;font-size:11px">Better <span class="accent">Nutrient</span></div>
  <p class="tiny" style="left:26px;top:62px;width:135px">Healthy recipes explained simply so every member can plan balanced meals at home with confidence and enjoy each new lesson.</p>
  <div style="left:26px;top:100px;font-size:6.5px;font-weight:700;color:var(--orange)">768K</div>
  <div style="left:73px;top:100px;font-size:6.5px;font-weight:700;color:var(--orange)">423K</div>
  <div style="left:120px;top:100px;font-size:6.5px;font-weight:700;color:var(--orange)">135K</div>
  <div style="left:26px;top:108px;font-size:4px;font-weight:600">Users</div>
  <div style="left:73px;top:108px;font-size:4px;font-weight:600">Classes</div>
  <div style="left:120px;top:108px;font-size:4px;font-weight:600">Chefs</div>
  <div class="motif-cool" aria-hidden="true" style="left:204px;top:40px;width:50px;height:48px;border:1.5px solid #fff;outline:1px solid #999"></div>
  <div class="h-sans" style="left:264px;top:45px;font-size:9.5px;line-height:12px">Lorem<br><span class="accent">Dolor Sit</span><br>Consectetuer</div>
  <div class="chip" style="left:204px;top:107px;width:155px;height:25px;font-size:9px;font-weight:500;line-height:25px;padding-left:11px">Know Food Better</div>
  <div style="left:75px;top:133px;width:8px;height:69px;background:var(--orange)"></div>
  <div style="left:337px;top:133px;width:22px;height:69px;background:var(--orange)"></div>
  <div class="motif-stripe" aria-hidden="true" style="left:83px;top:133px;width:254px;height:69px"></div>
  <div class="site">www.website.com</div><div class="page" style="color:#fff">3</div>
</section>

<section class="slide row2 col2">
  <div class="brand-bar"></div><div class="brand">Simmerly</div>
  <div style="left:0;width:359px;top:64px;text-align:center;font-size:36px;font-weight:700;line-height:42px">Eat <span class="chip" style="padding:0 6px">Well</span></div>
  <div style="left:0;width:359px;top:119px;text-align:center;font-size:8.5px;font-weight:500">Make Your Own Meal</div>
  <p class="tiny" style="left:60px;top:134px;width:239px;text-align:center">Pick a recipe, join a live chef and cook a full meal step by step from your own kitchen at home tonight.</p>
  <div class="site">www.website.com</div><div class="page">4</div>
</section>

<section class="slide row2 col3">
  <div class="brand-bar"></div><div class="brand">Simmerly</div>
  <div class="motif-cool" aria-hidden="true" style="left:11px;top:73px;width:299px;height:91px"></div>
  <div class="chip h-sans" style="left:26px;top:37px;width:66px;height:65px;font-size:12px;line-height:16px;text-align:center;padding-top:7px;color:var(--ink)">What<br>We<br>Have</div>
  <div style="left:112px;top:37px;font-size:6px;font-weight:600"><span class="accent">1.</span> Live Classes</div>
  <p class="tiny" style="left:120px;top:45px;width:75px">Chefs teach live sessions you can join daily.</p>
  <div style="left:211px;top:37px;font-size:6px;font-weight:600"><span class="accent">2.</span> Recipe Library</div>
  <p class="tiny" style="left:219px;top:45px;width:75px">Saved lessons to replay at your own pace.</p>
  <div class="site">www.website.com</div><div class="page">5</div>
</section>

<!-- Row 3 -->
<section class="slide row3 col1">
  <div class="brand-bar"></div><div class="brand">Simmerly</div>
  <div class="h-sans" style="left:24px;top:77px;font-size:15px;line-height:19px">Text<br><span class="accent">Added</span><br>Here</div>
  <div class="motif-warm" aria-hidden="true" style="left:99px;top:15px;width:108px;height:172px"></div>
  <div aria-hidden="true" style="left:128px;top:36px;width:50px;height:100px;border-radius:8px;background:var(--ink);padding:4px">
    <div style="width:100%;height:100%;border-radius:5px;background:var(--orange)"></div>
  </div>
  <div class="chip icon-box" style="left:197px;top:44px"><svg width="11" height="9"><circle cx="3" cy="3" r="2" fill="#fff"/><circle cx="8" cy="3" r="2" fill="#fff"/><rect x="0" y="6" width="11" height="3" rx="1.5" fill="#fff"/></svg></div>
  <div class="chip icon-box" style="left:197px;top:89px"><svg width="10" height="11"><circle cx="3" cy="2" r="1.6" fill="#fff"/><circle cx="7" cy="2" r="1.6" fill="#fff"/><rect x="1.5" y="4" width="3" height="7" fill="#fff"/><rect x="5.5" y="4" width="3" height="7" fill="#fff"/></svg></div>
  <div class="chip icon-box" style="left:197px;top:134px"><svg width="10" height="9"><path d="M5 9 L1 5 A2.3 2.3 0 0 1 5 2 A2.3 2.3 0 0 1 9 5 Z" fill="#fff"/></svg></div>
  <div style="left:228px;top:45px;font-size:6px;font-weight:600">We Before Me</div>
  <p class="tiny" style="left:228px;top:53px;width:85px">We put the home cook first in every feature.</p>
  <div style="left:227px;top:91px;font-size:6px;font-weight:600">We Are Good People</div>
  <p class="tiny" style="left:227px;top:99px;width:85px">Kind chefs who enjoy teaching new cooks.</p>
  <div style="left:227px;top:136px;font-size:6px;font-weight:600">We Work with Heart</div>
  <p class="tiny" style="left:227px;top:144px;width:85px">Every class is built with care and passion.</p>
  <div class="site">www.website.com</div><div class="page">6</div>
</section>

<section class="slide row3 col2">
  <div style="left:0;top:0;width:46px;height:202px;background:var(--ink)"></div>
  <div style="left:14px;top:160px;transform:rotate(-90deg);transform-origin:0 0;color:#fff;font-size:12px;font-weight:700;white-space:nowrap;width:130px">Featured Classes</div>
  <div class="motif-cool" aria-hidden="true" style="left:87px;top:0;width:118px;height:202px"></div>
  <div class="motif-soft" aria-hidden="true" style="left:242px;top:0;width:117px;height:202px"></div>
  <div class="chip" style="left:59px;top:15px;width:68px;height:68px;border-radius:50%;text-align:center;padding-top:16px">
    <div style="font-size:9px;font-weight:600">LIVE</div><div style="font-size:9px">Cook Along</div><div style="font-size:3.5px;line-height:4.4px">join a chef in<br>real time</div></div>
  <div class="chip" style="left:213px;top:15px;width:68px;height:68px;border-radius:50%;text-align:center;padding-top:16px">
    <div style="font-size:9px;font-weight:600">REPLAY</div><div style="font-size:9px">On Demand</div><div style="font-size:3.5px;line-height:4.4px">cook at your<br>own pace</div></div>
</section>

<section class="slide row3 col3">
  <div class="brand-bar"></div><div class="brand">Simmerly</div>
  <div class="motif-warm" aria-hidden="true" style="left:123px;top:0;width:236px;height:114px"></div>
  <div class="h-sans" style="left:24px;top:78px;font-size:21px;line-height:27px">Text<br><span class="accent">Added</span><br>Here</div>
  <div class="card" style="left:163px;top:80px;width:72px;height:90px"></div>
  <div class="chip" style="left:163px;top:80px;width:72px;height:16px;font-size:11px;font-weight:600;line-height:16px;text-align:center">Text Here</div>
  <p class="tiny" style="left:168px;top:100px;width:62px">Short video lessons guide each step with clear timers and tips.<br><br>Members cook along and share results with friends.</p>
  <div class="card" style="left:252px;top:80px;width:72px;height:90px"></div>
  <div class="chip" style="left:252px;top:80px;width:72px;height:16px;font-size:11px;font-weight:600;line-height:16px;text-align:center">Text Here</div>
  <p class="tiny" style="left:257px;top:100px;width:62px">Chefs earn income from classes they host each week online.<br><br>Reviews help the best lessons rise to the top.</p>
  <div class="site">www.website.com</div><div class="page">8</div>
</section>

<!-- Row 4 -->
<section class="slide row4 col1">
  <div class="brand-bar"></div><div class="brand">Simmerly</div>
  <svg style="left:26px;top:83px" width="40" height="42" aria-hidden="true"><polygon points="0,0 18,0 40,21 18,42 0,42 22,21" fill="#ebebeb"/></svg>
  <div class="motif-warm" aria-hidden="true" style="left:96px;top:32px;width:68px;height:80px"></div>
  <div class="motif-cool" aria-hidden="true" style="left:184px;top:32px;width:68px;height:80px"></div>
  <div class="motif-soft" aria-hidden="true" style="left:272px;top:32px;width:68px;height:80px"></div>
  <div style="left:272px;top:112px;width:48px;height:2px;background:var(--orange)"></div>
  <div style="left:96px;top:118px;font-size:6.5px;font-weight:700"><span class="accent">First</span> Option</div>
  <div style="left:184px;top:118px;font-size:6.5px;font-weight:700"><span class="accent">Second</span> Option</div>
  <div style="left:272px;top:118px;font-size:6.5px;font-weight:700"><span class="accent">Third</span> Option</div>
  <p class="tiny" style="left:96px;top:127px;width:50px">Free plan with weekly live classes and a small recipe set.</p>
  <p class="tiny" style="left:184px;top:127px;width:50px">Plus plan with the full library and chef chat access.</p>
  <p class="tiny" style="left:272px;top:127px;width:50px">Pro plan with private lessons and custom meal plans.</p>
  <div class="site">www.website.com</div><div class="page">9</div>
</section>

<section class="slide row4 col2">
  <div class="brand-bar"></div><div class="brand">Simmerly</div>
  <div class="motif-cool" aria-hidden="true" style="left:18px;top:43px;width:91px;height:129px"></div>
  <div class="motif-warm" aria-hidden="true" style="left:116px;top:43px;width:91px;height:129px"></div>
  <div class="serif" style="left:221px;top:74px;font-size:9px;font-weight:700">Online</div>
  <div class="serif accent" style="left:219px;top:82px;font-size:24px;font-weight:900">Cooking</div>
  <div class="serif" style="left:219px;top:108px;font-size:28px;font-weight:900">App</div>
  <div class="site">www.website.com</div><div class="page">10</div>
</section>

<section class="slide row4 col3">
  <div class="brand-bar"></div><div class="brand">Simmerly</div>
  <div style="left:21px;top:46px;font-size:7px;font-weight:700;line-height:9px"><span class="accent">1st</span><br>Order</div>
  <p class="tiny" style="left:21px;top:66px;width:50px">Choose a class and pick a start time that suits you.</p>
  <div style="left:84px;top:104px;font-size:7px;font-weight:700;line-height:9px"><span class="accent">2nd</span><br>Order</div>
  <p class="tiny" style="left:84px;top:124px;width:50px">Gather items from the list and cook live with the chef.</p>
  <div style="left:154px;top:36px;width:153px;height:103px;background:#3a3a3a;border-radius:3px"></div>
  <div style="left:157px;top:39px;width:147px;height:89px;background:var(--navy)"></div>
  <div class="motif-warm" aria-hidden="true" style="left:248px;top:39px;width:56px;height:89px"></div>
  <div style="left:166px;top:49px;font-size:6px;color:#fff">Simmerly</div>
  <div class="serif accent" style="left:166px;top:76px;font-size:9px;font-weight:900">Online</div>
  <div class="serif" style="left:166px;top:87px;font-size:12px;font-weight:900;color:#fff">Cooking</div>
  <div class="chip" style="left:229px;top:120px;width:102px;height:13px;font-size:8px;font-weight:600;line-height:13px;text-align:center">Make Your Meal</div>
  <div style="left:154px;top:139px;width:153px;height:7px;background:#dcdcdc"></div>
  <svg style="left:207px;top:146px" width="48" height="20" aria-hidden="true"><polygon points="18,0 30,0 33,16 15,16" fill="#cfcfcf"/><rect x="5" y="16" width="38" height="2" fill="#bbb"/></svg>
  <div class="site">www.website.com</div><div class="page">11</div>
</section>

<!-- Row 5 -->
<section class="slide row5 col1">
  <div class="brand-bar"></div><div class="brand">Simmerly</div>
  <div style="left:217px;top:39px;width:142px;height:124px;background:var(--orange)"></div>

  <div class="chip food-card" style="left:30px;top:57px"></div>
  <div class="food-icon" style="left:36px;top:66px;border-color:#fff;border-radius:50%"></div>
  <div class="food-title" style="left:52px;top:63px;color:#fff">Food</div>
  <div class="food-text" style="left:52px;top:71px;color:#fff">Fresh ideas for meals every week</div>

  <div class="card food-card" style="left:107px;top:57px"></div>
  <div class="food-icon" style="left:113px;top:66px;border-radius:2px"></div>
  <div class="food-title" style="left:129px;top:63px">Food</div>
  <div class="food-text" style="left:129px;top:71px">Fresh ideas for meals every week</div>

  <div class="card food-card" style="left:184px;top:57px"></div>
  <div class="food-icon" style="left:190px;top:66px;border-radius:50%"></div>
  <div class="food-title" style="left:206px;top:63px">Food</div>
  <div class="food-text" style="left:206px;top:71px">Fresh ideas for meals every week</div>

  <div class="card food-card" style="left:260px;top:57px"></div>
  <div class="food-icon" style="left:266px;top:66px;border-radius:2px"></div>
  <div class="food-title" style="left:282px;top:63px">Food</div>
  <div class="food-text" style="left:282px;top:71px">Fresh ideas for meals every week</div>

  <div class="card food-card" style="left:30px;top:106px"></div>
  <div class="food-icon" style="left:36px;top:115px;border-radius:50%"></div>
  <div class="food-title" style="left:52px;top:112px">Food</div>
  <div class="food-text" style="left:52px;top:120px">Fresh ideas for meals every week</div>

  <div class="card food-card" style="left:107px;top:106px"></div>
  <div class="food-icon" style="left:113px;top:115px;border-radius:2px"></div>
  <div class="food-title" style="left:129px;top:112px">Food</div>
  <div class="food-text" style="left:129px;top:120px">Fresh ideas for meals every week</div>

  <div class="card food-card" style="left:184px;top:106px"></div>
  <div class="food-icon" style="left:190px;top:115px;border-radius:50%"></div>
  <div class="food-title" style="left:206px;top:112px">Food</div>
  <div class="food-text" style="left:206px;top:120px">Fresh ideas for meals every week</div>

  <div class="card food-card" style="left:260px;top:106px"></div>
  <div class="food-icon" style="left:266px;top:115px;border-radius:2px"></div>
  <div class="food-title" style="left:282px;top:112px">Food</div>
  <div class="food-text" style="left:282px;top:120px">Fresh ideas for meals every week</div>

  <div class="site">www.website.com</div><div class="page">12</div>
</section>

<section class="slide row5 col2">
  <div class="brand-bar"></div><div class="brand">Simmerly</div>
  <div class="serif" style="left:0;width:359px;top:47px;text-align:center;font-size:17px;font-weight:900">Text <span class="accent">Added</span> Here</div>
  <div class="card" style="left:31px;top:88px;width:296px;height:72px"></div>
  <div class="motif-cool" aria-hidden="true" style="left:124px;top:88px;width:107px;height:72px"></div>
  <div class="accent" style="left:39px;top:95px;font-size:11px;font-weight:600">Text Here</div>
  <p class="tiny" style="left:39px;top:110px;width:78px;font-size:4px;line-height:5px">Home cooks learn from pros in live rooms, ask questions and get feedback on each dish they make.</p>
  <div class="accent" style="left:245px;top:95px;font-size:11px;font-weight:600">Text Here</div>
  <p class="tiny" style="left:245px;top:110px;width:78px;font-size:4px;line-height:5px">Chefs build a following, host paid classes and sell recipe packs directly to their own fans.</p>
  <div class="site">www.website.com</div><div class="page">13</div>
</section>

<section class="slide row5 col3">
  <div class="motif-warm" aria-hidden="true" style="left:30px;top:0;width:134px;height:202px"></div>
  <div style="left:185px;top:44px;font-size:20px;font-weight:500">Simmerly</div>
  <svg style="left:185px;top:88px" width="12" height="70" aria-hidden="true">
    <path d="M2 2c1-1 3-1 4 1l1 2c0 1-1 2-1 2 1 2 2 3 4 4 0 0 1-1 2-1l2 1c2 1 2 3 1 4-2 2-5 2-8 0S1 9 1 5z" fill="#ff3800"/>
    <polygon points="1,30 11,26 7,36 6,31" fill="#ff3800"/>
    <path d="M6 52 L12 58 H10 V63 H2 V58 H0 Z" fill="#ff3800"/>
  </svg>
  <div style="left:200px;top:88px;width:1px;height:12px;background:var(--ink)"></div>
  <div style="left:200px;top:113px;width:1px;height:12px;background:var(--ink)"></div>
  <div style="left:200px;top:139px;width:1px;height:12px;background:var(--ink)"></div>
  <div style="left:205px;top:87px;font-size:6px;line-height:8px;color:#555">+1 555 0142 3388<br>+1 555 0142 3389</div>
  <div style="left:205px;top:112px;font-size:6px;line-height:8px;color:#555">www.websitename.com<br>urname@email.com</div>
  <div style="left:205px;top:138px;font-size:6px;line-height:8px;color:#555">1234 Street name, town/city,<br>state/country, post/zip 012345.</div>
</section>

</body>
</html>
```